Keystone Haulers Billboard design

I need two billboard designs using our logo and adding a few words Looking for a black background with our logo and wording in either purple or white.

need it to have our website keystonehaulers-example.com. phone number 555 201 4387

Also have 16/20/30 yard dumpsters available!

one billboard is size 7x21 feet the other is 15x 21 ft

Target Market(s)

Contractors, home owners

Requirements
Must have
• Use font similar to logo that is eye catching

```html
<!DOCTYPE html>
<html lang="en">
<head>
<meta charset="utf-8">
<title>Keystone Haulers Billboard 15x21</title>
<link href="https://fonts.googleapis.com/css2?family=Montserrat:wght@400;500;600;700;800&display=swap" rel="stylesheet">
<style>
  :root {
    --page: #b9b9b9;
    --black: #070707;
    --white: #ffffff;
    --purple: #7f3d9e;
    --purple-deep: #3a1650;
    --ink: #0b0b0b;
  }
  * { box-sizing: border-box; margin: 0; padding: 0; }
  html, body { width: 1200px; height: 895px; overflow: hidden; }
  body {
    background: var(--page);
    font-family: "Montserrat", sans-serif;
    position: relative;
  }
  .billboard {
    position: absolute;
    left: 20px; top: 33px;
    width: 1160px; height: 828px;
    background: var(--white);
    overflow: hidden;
  }
  .hero {
    position: absolute; left: 0; top: 0;
    width: 1160px; height: 619px;
    background: var(--black);
  }
  .hero-photo {
    position: absolute; left: 539px; top: 112px;
    width: 621px; height: 507px;
    background:
      radial-gradient(ellipse at 75% 5%, #f2f2f2 0%, #b8b8b8 30%, rgba(60,60,60,0.6) 60%, rgba(7,7,7,0) 85%),
      linear-gradient(90deg, var(--black) 0%, #1a1a1a 30%, #4a4a4a 70%, #6d6d6d 100%);
  }
  .web-tab {
    position: absolute; left: 690px; top: 112px;
    width: 420px; height: 32px;
    background: var(--black);
    border-radius: 0 0 12px 12px;
    display: flex; align-items: center; gap: 9px;
    padding-left: 22px;
    color: var(--white);
    font-size: 20px; font-weight: 700;
    white-space: nowrap;
  }
  .web-tab .dot {
    width: 18px; height: 18px; border-radius: 50%;
    background: var(--purple);
    flex: none;
  }
  .web-tab .tld { font-weight: 500; }
  .brand-name {
    position: absolute; left: 66px; top: 62px;
    color: var(--white);
    font-weight: 800; font-size: 44px; line-height: 44px;
    letter-spacing: 1px; text-transform: uppercase;
  }
  .headline {
    position: absolute; left: 66px; top: 196px;
    color: var(--white);
    font-weight: 800; font-size: 67px; line-height: 64px;
    letter-spacing: -1px; text-transform: uppercase;
  }
  .divider {
    position: absolute; left: 67px; top: 467px;
    width: 502px; height: 2px;
    background: linear-gradient(90deg, var(--purple), rgba(127,61,158,0.2));
  }
  .sizes {
    position: absolute; left: 66px; top: 482px;
    color: var(--white);
    font-weight: 500; font-size: 39px; line-height: 48px;
    letter-spacing: -0.5px;
  }
  .sizes .accent { color: var(--purple); font-weight: 700; }
  .tagline-band {
    position: absolute; left: 0; top: 619px;
    width: 1160px; height: 48px;
    background: linear-gradient(90deg, var(--purple-deep) 0%, var(--purple) 12%, var(--purple) 88%, var(--purple-deep) 100%);
    color: var(--white);
    font-weight: 700; font-size: 29px; line-height: 48px;
    padding-left: 66px; letter-spacing: -0.3px;
    white-space: nowrap;
  }
  .cta-row {
    position: absolute; left: 66px; top: 694px;
    display: flex; align-items: center;
  }
  .book-now {
    position: relative; width: 272px; height: 52px;
  }
  .book-now svg { position: absolute; left: 0; top: 0; }
  .book-now span {
    position: absolute; left: 17px; top: 0;
    line-height: 52px;
    color: var(--purple);
    font-weight: 800; font-size: 33px;
    white-space: nowrap;
  }
  .phone-icon { margin-left: 24px; width: 40px; height: 40px; }
  .call {
    margin-left: 12px;
    color: var(--ink);
    font-size: 43px; font-weight: 500; letter-spacing: -0.5px;
    white-space: nowrap;
  }
  .call strong { font-weight: 800; }
</style>
</head>
<body>
  <main class="billboard">
    <section class="hero">
      <div class="hero-photo" role="img" aria-label="Black roll-off dumpster being unloaded from a white pickup truck on a gravel lot"></div>
      <div class="web-tab"><span class="dot"></span><span>keystonehaulers-example<span class="tld">.com</span></span></div>
      <div class="brand-name">Keystone<br>Haulers</div>
      <h1 class="headline">Residential &amp;<br>Commercial<br>Dumpster<br>Rentals</h1>
      <div class="divider"></div>
      <p class="sizes">Also have <span class="accent">16/20/30</span><br><span class="accent">Yard Dumpsters</span> available!</p>
    </section>
    <div class="tagline-band">Ridgeford’s top choice for reliable dumpster rentals &amp; junk removal.</div>
    <div class="cta-row">
      <div class="book-now">
        <svg width="272" height="52" viewBox="0 0 272 52">
          <path d="M1 1 H253 L270 26 L253 51 H1 Z" fill="none" stroke="#7f3d9e" stroke-width="1.5"/>
        </svg>
        <span>BOOK NOW!</span>
      </div>
      <svg class="phone-icon" viewBox="0 0 40 40" aria-hidden="true">
        <circle cx="20" cy="20" r="20" fill="#7f3d9e"/>
        <path d="M14 11c1-1 2.4-.8 3 .4l1.6 3c.5 1 .2 1.9-.6 2.5l-1 .8c.9 2.2 2.7 4 4.9 4.9l.8-1c.6-.8 1.5-1.1 2.5-.6l3 1.6c1.2.6 1.4 2 .4 3l-1.5 1.5c-1 1-2.6 1.3-4 .7-5.2-2-9.3-6.1-11.3-11.3-.6-1.4-.3-3 .7-4z" fill="#0b0b0b"/>
      </svg>
      <div class="call">Call <strong>555 201 4387</strong></div>
    </div>
  </main>
</body>
</html>
```